Company Proposal Powerpoint Template

We would like to update our overall proposal presentation with a fresh, new look that might appeal to the younger generation. We are a full-meeting management company that specializes in corporate events sales meetings, incentive trips, and tradeshows/conferences.
We have a core set of slides that we use for presentations, but will also need to customize based on the customers we service and what we are selling each potential client.
We have a company logo, but we are not tied into the colors schemes for the logo and are okay adding the logo in black or white versus in color.
I have included our current look and feel for this presentation. This will also give you content that we typically add to this presentation.
Reason: Traveling out of the office so limited access to review the art.
Industry/Entity Type
It Company
Look and feel
Each slider illustrates characteristics of the customer's brand and the style your logo design should communicate.

```html
<!DOCTYPE html>
<html lang="en">
<head>
<meta charset="utf-8">
<title>Harborline Events – Proposal Deck</title>
<link href="https://fonts.googleapis.com/css2?family=Libre+Baskerville:wght@400;700&family=Roboto:wght@400;500;700&display=swap" rel="stylesheet">
<style>
:root{
  --red:#d6264e;
  --taupe:#8b8278;
  --taupe-dark:#6e665d;
  --grey:#b5b1ac;
  --ink:#4d4d4d;
  --muted:#a3a3a3;
  --paper:#ffffff;
  --canvas:#f4f4f4;
}
*{box-sizing:border-box;margin:0;padding:0}
html,body{width:824px;height:1200px;overflow:hidden;background:var(--canvas)}
body{font-family:"Roboto",Arial,sans-serif;color:var(--ink)}
.deck{display:grid;grid-template-columns:repeat(3,264px);grid-auto-rows:196px;column-gap:8px;row-gap:4px;padding:2px 8px}
.slide{position:relative;overflow:hidden;background:var(--paper);box-shadow:0 0 2px rgba(0,0,0,.3)}
.abs{position:absolute}
.title{position:absolute;left:12px;top:12px;font:400 10.5px "Libre Baskerville",Georgia,serif;color:#5b5b5b}
.title::after{content:"";position:absolute;left:0;bottom:-5px;width:18px;height:1px;background:var(--red)}
.brand{position:absolute;top:6px;right:7px;display:flex;align-items:center;gap:2px;font:400 4.6px "Libre Baskerville",Georgia,serif;color:#8d8d8d}
.brand i{display:block;width:5px;height:5px;border:.6px solid currentColor}
.brand.light{color:#fff}
.footer{position:absolute;left:0;right:9px;bottom:5px;height:7px;background:var(--taupe);color:#fff;font:400 3.3px "Libre Baskerville",serif;display:flex;align-items:center;justify-content:space-between;padding:0 5px}
.footer::after{content:"";position:absolute;right:-9px;top:-1px;width:9px;height:9px;background:var(--red)}
.lorem{font-size:3.6px;line-height:1.4;color:var(--muted)}
.lorem+.lorem{margin-top:3px}
.lorem.light{color:#efe9e3}
.intro{position:absolute;left:12px;top:45px;font-size:7.2px;font-weight:500;color:#555;line-height:1.35}
.intro b{color:var(--red);font-weight:700}
.serif-head{font:700 5.6px "Libre Baskerville",serif;color:#6a6a6a;margin-bottom:3px}
.bt{display:block;font-size:4.4px;font-weight:500;color:#6a6a6a;margin-bottom:1px}
.ico{width:13px;height:13px;flex:none}
.bullet{position:absolute;display:flex;gap:5px;align-items:flex-start;width:82px}
.bullet .lorem{font-size:3.2px}
.col{position:absolute}
.photo{position:absolute}
.center{text-align:center}
.vcol{position:absolute;display:flex;flex-direction:column;align-items:center;text-align:center}
</style>
</head>
<body>
<svg width="0" height="0" style="position:absolute" aria-hidden="true">
  <defs>
    <symbol id="g-search" viewBox="0 0 20 20"><circle cx="10" cy="10" r="10" fill="#d6264e"/><circle cx="9" cy="9" r="3.4" fill="none" stroke="#fff" stroke-width="1.6"/><path d="M11.5 11.5l3 3" stroke="#fff" stroke-width="1.8" stroke-linecap="round"/></symbol>
    <symbol id="g-heart" viewBox="0 0 20 20"><circle cx="10" cy="10" r="10" fill="#d6264e"/><path d="M10 14.5l-4-4a2.3 2.3 0 014-2.6 2.3 2.3 0 014 2.6z" fill="#fff"/></symbol>
    <symbol id="g-gear" viewBox="0 0 20 20"><circle cx="10" cy="10" r="10" fill="#d6264e"/><circle cx="10" cy="10" r="4" fill="none" stroke="#fff" stroke-width="2" stroke-dasharray="2 1.2"/><circle cx="10" cy="10" r="1.4" fill="#fff"/></symbol>
    <symbol id="g-pen" viewBox="0 0 20 20"><circle cx="10" cy="10" r="10" fill="#d6264e"/><path d="M6.5 13.5l1-3 5-5 2 2-5 5z" fill="#fff"/></symbol>
    <symbol id="g-chart" viewBox="0 0 20 20"><circle cx="10" cy="10" r="10" fill="#d6264e"/><path d="M6.5 14V11M9 14V8.5M11.5 14V10M14 14V6.5" stroke="#fff" stroke-width="1.6"/></symbol>
    <symbol id="g-people" viewBox="0 0 20 20"><circle cx="10" cy="10" r="10" fill="#d6264e"/><circle cx="8" cy="8" r="1.8" fill="#fff"/><circle cx="12.5" cy="8.5" r="1.5" fill="#fff"/><path d="M5 14a3 3 0 016 0zM10 14a2.6 2.6 0 015.2 0z" fill="#fff"/></symbol>
  </defs>
</svg>

<main class="deck">

<!-- 1 Two Column Description -->
<section class="slide">
  <h2 class="title">Two Column Description</h2>
  <div class="brand"><i></i>Harborline</div>
  <p class="intro">We are <b>Harborline</b><br>Taking Services to a New Level of Excellence</p>
  <div class="col" style="left:12px;top:84px;width:112px">
    <p class="lorem">Lorem ipsum dolor sit amet, consectetur adipiscing elit, sed do eiusmod tempor incididunt ut labore et dolore magna aliqua. Ut enim ad minim veniam, quis nostrud exercitation ullamco laboris nisi ut aliquip ex ea commodo consequat.</p>
    <p class="lorem">Duis aute irure dolor in reprehenderit in voluptate velit esse cillum dolore eu fugiat nulla pariatur. Excepteur sint occaecat cupidatat non proident, sunt in culpa qui officia deserunt mollit anim id est laborum.</p>
  </div>
  <div class="col" style="left:140px;top:84px;width:112px">
    <p class="lorem">Lorem ipsum dolor sit amet, consectetur adipiscing elit, sed do eiusmod tempor incididunt ut labore et dolore magna aliqua. Ut enim ad minim veniam, quis nostrud exercitation ullamco laboris nisi ut aliquip ex ea commodo consequat.</p>
    <p class="lorem">Duis aute irure dolor in reprehenderit in voluptate velit esse cillum dolore eu fugiat nulla pariatur. Excepteur sint occaecat cupidatat non proident, sunt in culpa qui officia deserunt mollit anim id est laborum.</p>
  </div>
  <div class="footer"><span>Harborline © 2016 All rights reserved.</span><span>37</span></div>
</section>

<!-- 2 Divider -->
<section class="slide">
  <div class="photo" role="img" aria-label="Muted hotel lobby photograph" style="inset:0;background:linear-gradient(160deg,#9a9086,#7c7369 60%,#6a6158)"></div>
  <div class="abs" style="top:24px;right:34px;display:flex;align-items:center;gap:3px;font:400 7.5px 'Libre Baskerville',serif;color:#fff"><i style="display:block;width:8px;height:8px;border:.8px solid #fff"></i>Harborline Events</div>
  <div class="abs center" style="left:0;right:0;top:123px;height:48px;background:var(--red);color:#fff;padding-top:7px">
    <div style="font-size:5px">Divider Page</div>
    <div style="font:700 10.5px 'Libre Baskerville',serif;margin:2px 0">Your Title Goes Here</div>
    <div style="font:400 6px 'Libre Baskerville',serif;opacity:.9">Your Subtitle Here</div>
  </div>
</section>

<!-- 3 Three Column Description -->
<section class="slide">
  <h2 class="title">Three Column Description</h2>
  <div class="brand"><i></i>Harborline</div>
  <p class="intro">We are <b>Harborline</b><br>Taking Services to a New Level of Excellence</p>
  <div class="col" style="left:12px;top:84px;width:72px"><p class="lorem">Lorem ipsum dolor sit amet, consectetur adipiscing elit, sed do eiusmod tempor incididunt ut labore et dolore magna dolore aliqua.</p><p class="lorem">Ut enimad minim veniam, quis nostrud exercitation ullamco laboris nisi ut aliquip ex ea commodo dolor consequat.</p></div>
  <div class="col" style="left:98px;top:84px;width:72px"><p class="lorem">Lorem ipsum dolor sit amet, consectetur adipiscing elit, sed do eiusmod tempor incididunt ut labore et dolore magna dolore aliqua.</p><p class="lorem">Ut enimad minim veniam, quis nostrud exercitation ullamco laboris nisi ut aliquip ex ea commodo dolor consequat.</p></div>
  <div class="col" style="left:184px;top:84px;width:72px"><p class="lorem">Lorem ipsum dolor sit amet, consectetur adipiscing elit, sed do eiusmod tempor incididunt ut labore et dolore magna dolore aliqua.</p><p class="lorem">Ut enimad minim veniam, quis nostrud exercitation ullamco laboris nisi ut aliquip ex ea commodo dolor consequat.</p></div>
  <div class="footer"><span>Harborline © 2016 All rights reserved.</span><span>39</span></div>
</section>

<!-- 4 Photo with icon bullets -->
<section class="slide">
  <div class="photo" role="img" aria-label="Stone building facade photograph" style="left:0;right:0;top:0;height:104px;background:linear-gradient(180deg,#8c8379,#6f675e)"></div>
  <div class="abs" style="left:20px;top:40px;display:flex;align-items:center;gap:3px;font:400 7px 'Libre Baskerville',serif;color:#fff"><i style="display:block;width:8px;height:8px;border:.8px solid #fff"></i>Harborline Events</div>
  <div class="abs" style="left:132px;top:44px;width:120px">
    <div style="font:700 6px 'Libre Baskerville',serif;color:#fff;margin-bottom:8px">Your Title Goes Here</div>
    <p class="lorem light" style="font-size:3.8px">Lorem ipsum dolor sit amet, consectetur adipiscing elit, sed do eiusmod tempor incididunt ut labore et commodo consequat dolore magna aliqua. Duis aute irure dolor in reprehenderit in voluptate velit esse cillum dolore.</p>
  </div>
  <div class="photo" role="img" aria-label="Hotel exterior at dusk photograph" style="left:14px;top:80px;width:86px;height:68px;border:2px solid #fff;background:linear-gradient(180deg,#3d5a8c,#5a4e4a 70%,#3a322c)"></div>
  <div class="bullet" style="left:123px;top:118px;width:60px"><svg class="ico"><use href="#g-search"/></svg><div><b class="bt">Your Text Here</b><p class="lorem">Lorem ipsum dolor sit amet, consectetur adipiscing elit, sed do.</p></div></div>
  <div class="bullet" style="left:195px;top:118px;width:62px"><svg class="ico"><use href="#g-heart"/></svg><div><b class="bt">Your Text Here</b><p class="lorem">Lorem ipsum dolor sit amet, consectetur adipiscing elit, sed do.</p></div></div>
  <div class="bullet" style="left:123px;top:148px;width:60px"><svg class="ico"><use href="#g-gear"/></svg><div><b class="bt">Your Text Here</b><p class="lorem">Lorem ipsum dolor sit amet, consectetur adipiscing elit, sed do.</p></div></div>
  <div class="bullet" style="left:195px;top:148px;width:62px"><svg class="ico"><use href="#g-pen"/></svg><div><b class="bt" style="color:var(--red)">Your Text Here</b><p class="lorem">Lorem ipsum dolor sit amet, consectetur adipiscing elit, sed do.</p></div></div>
  <div class="footer"><span>Harborline © 2016 All rights reserved.</span><span>40</span></div>
</section>

<!-- 5 Multiple Column Area -->
<section class="slide">
  <h2 class="title">Multiple Column Area</h2>
  <div class="brand"><i></i>Harborline</div>
  <div class="vcol" style="left:8px;top:50px;width:48px"><svg class="ico"><use href="#g-gear"/></svg><b class="bt" style="margin-top:3px">Your Text Here</b><p class="lorem">Lorem ipsum consectetur adipiscing elit.</p></div>
  <div class="vcol" style="left:60px;top:50px;width:48px"><svg class="ico"><use href="#g-pen"/></svg><b class="bt" style="margin-top:3px">Your Text Here</b><p class="lorem">Lorem ipsum consectetur adipiscing elit.</p></div>
  <div class="vcol" style="left:112px;top:50px;width:48px"><svg class="ico"><use href="#g-search"/></svg><b class="bt" style="margin-top:3px">Your Text Here</b><p class="lorem">Lorem ipsum consectetur adipiscing elit.</p></div>
  <div class="vcol" style="left:164px;top:50px;width:48px"><svg class="ico"><use href="#g-pen"/></svg><b class="bt" style="margin-top:3px">Your Text Here</b><p class="lorem">Lorem ipsum consectetur adipiscing elit.</p></div>
  <div class="vcol" style="left:216px;top:50px;width:48px"><svg class="ico"><use href="#g-chart"/></svg><b class="bt" style="margin-top:3px">Your Text Here</b><p class="lorem">Lorem ipsum consectetur adipiscing elit.</p></div>
  <div class="col" style="left:17px;top:120px;width:112px"><div class="serif-head">Your Title Goes Here</div><p class="lorem">Lorem ipsum dolor sit amet, consectetur adipiscing elit, sed do eiusmod tempor incididunt ut labore et commodo consequat dolore magna aliqua.</p><p class="lorem">Duis aute irure dolor in reprehenderit in voluptate velit esse cillum dolore eu fugiat nulla pariatur.</p></div>
  <div class="col" style="left:145px;top:120px;width:112px"><div class="serif-head">Your Title Goes Here</div><p class="lorem">Lorem ipsum dolor sit amet, consectetur adipiscing elit, sed do eiusmod tempor incididunt ut labore et commodo consequat dolore magna aliqua.</p><p class="lorem">Duis aute irure dolor in reprehenderit in voluptate velit esse cillum dolore eu fugiat nulla pariatur.</p></div>
  <div class="footer"><span>Harborline © 2016 All rights reserved.</span><span>41</span></div>
</section>

<!-- 6 Our Differences -->
<section class="slide">
  <h2 class="title">Our Differences</h2>
  <div class="brand"><i></i>Harborline</div>
  <div class="abs" style="left:0;right:0;top:59px;height:100px;background:var(--taupe)"></div>
  <div class="bullet" style="left:12px;top:70px;width:115px;align-items:center"><svg class="ico"><use href="#g-pen"/></svg><p class="lorem light" style="font-size:3.8px">Lorem ipsum dolor sit amet, consectetur adipiscing elit, sed do labore.</p></div>
  <div class="bullet" style="left:12px;top:90px;width:115px;align-items:center"><svg class="ico"><use href="#g-search"/></svg><p class="lorem light" style="font-size:3.8px">Duis aute irure dolor in reprehenderit in voluptate velit esse cillum dolore.</p></div>
  <div class="bullet" style="left:12px;top:110px;width:115px;align-items:center"><svg class="ico"><use href="#g-pen"/></svg><p class="lorem light" style="font-size:3.8px">Lorem ipsum dolor sit amet, consectetur adipiscing elit, sed do labore.</p></div>
  <div class="bullet" style="left:12px;top:130px;width:115px;align-items:center"><svg class="ico"><use href="#g-search"/></svg><p class="lorem light" style="font-size:3.8px">Duis aute irure dolor in reprehenderit in voluptate velit esse cillum dolore.</p></div>
  <div class="photo" role="img" aria-label="Conference room with long table photograph" style="left:136px;top:68px;width:120px;height:82px;background:linear-gradient(180deg,#e4e2df,#9a948d 60%,#5c5650)"></div>
  <div class="footer"><span>Harborline © 2016 All rights reserved.</span><span>42</span></div>
</section>

<!-- 7 Four Bullets with Paragraph -->
<section class="slide">
  <h2 class="title">Four Bullets with Paragraph</h2>
  <div class="brand"><i></i>Harborline</div>
  <div class="bullet" style="left:12px;top:62px;width:68px"><svg class="ico"><use href="#g-search"/></svg><div><b class="bt">Your Text Here</b><p class="lorem">Lorem ipsum dolor sit amet, consectetur adipiscing elit, sed do eiusmod.</p></div></div>
  <div class="bullet" style="left:82px;top:62px;width:68px"><svg class="ico"><use href="#g-heart"/></svg><div><b class="bt">Your Text Here</b><p class="lorem">Lorem ipsum dolor sit amet, consectetur adipiscing elit, sed do eiusmod.</p></div></div>
  <div class="bullet" style="left:12px;top:118px;width:68px"><svg class="ico"><use href="#g-gear"/></svg><div><b class="bt">Your Text Here</b><p class="lorem">Lorem ipsum dolor sit amet, consectetur adipiscing elit, sed do eiusmod.</p></div></div>
  <div class="bullet" style="left:82px;top:118px;width:68px"><svg class="ico"><use href="#g-pen"/></svg><div><b class="bt">Your Text Here</b><p class="lorem">Lorem ipsum dolor sit amet, consectetur adipiscing elit, sed do eiusmod.</p></div></div>
  <div class="col" style="left:160px;top:63px;width:96px"><div class="serif-head">Your Title Goes Here</div><p class="lorem">Lorem ipsum dolor sit amet, consectetur adipiscing elit, sed do eiusmod tempor incididunt ut labore et commodo consequat dolore magna aliqua.</p><p class="lorem">Duis aute irure dolor in reprehenderit in voluptate velit esse cillum dolore eu fugiat nulla pariatur.</p><p class="lorem">Ut enimad minim veniam, quis nostrud exercitation ullamco laboris nisi ut aliquip ex ea commodo consequat.</p></div>
  <div class="footer"><span>Harborline © 2016 All rights reserved.</span><span>43</span></div>
</section>

<!-- 8 Coffee Break -->
<section class="slide">
  <div class="photo" role="img" aria-label="Coffee cup on a table in dim light photograph" style="inset:0;background:radial-gradient(ellipse at 55% 70%,#4a443d,#7a7167 45%,#8e857b)"></div>
  <svg class="abs" style="left:123px;top:38px" width="18" height="18" viewBox="0 0 20 20" aria-hidden="true"><path d="M4 9h10v3a5 5 0 01-10 0z M14 10h2a2 2 0 010 4h-2" fill="none" stroke="#fff" stroke-width="1.6"/><path d="M4 18h10" stroke="#fff" stroke-width="1.4"/><path d="M8 3v3M11 3v3" stroke="#fff" stroke-width="1.2"/></svg>
  <div class="abs" style="left:24px;top:60px;font:700 11.5px 'Roboto',sans-serif;color:#fff;letter-spacing:.3px">COFFEE BREAK</div>
  <div class="abs" style="left:48px;top:74px;font:400 4.2px 'Libre Baskerville',serif;color:var(--red)">Back in 15 minutes</div>
</section>

<!-- 9 Paragraph with Three Bullet -->
<section class="slide">
  <h2 class="title">Paragraph with Three Bullet</h2>
  <div class="brand"><i></i>Harborline</div>
  <p class="intro">We are <b>Harborline</b><br>Taking Services to a New Level of Excellence</p>
  <div class="col" style="left:12px;top:80px;width:62px"><p class="lorem">Lorem ipsum dolor sit amet, consectetur adipiscing elit, sed do eiusmod tempor incididunt ut labore et dolore magna aliqua. Ut enimad minim veniam, quis nostrud exercitation ullamco laboris nisi ut aliquip ex ea commodo consequat.</p><p class="lorem">Duis aute irure dolor in reprehenderit in voluptate velit esse cillum dolore eu fugiat nulla pariatur excepteur occaecat.</p></div>
  <div class="vcol" style="left:80px;top:84px;width:56px"><svg class="ico"><use href="#g-search"/></svg><b class="bt" style="margin-top:3px">Your Text Here</b><p class="lorem">Lorem ipsum dolor sit amet, consectetur adipiscing elit, sed do eiusmod incididunt ut labore et aliqua.</p><p class="lorem">Ut enimad minim veniam, quis nostrud exercitation laboris nisi ut commodo consequat.</p></div>
  <div class="vcol" style="left:138px;top:84px;width:56px"><svg class="ico"><use href="#g-pen"/></svg><b class="bt" style="margin-top:3px">Your Text Here</b><p class="lorem">Lorem ipsum dolor sit amet, consectetur adipiscing elit, sed do eiusmod incididunt ut labore et aliqua.</p><p class="lorem">Ut enimad minim veniam, quis nostrud exercitation laboris nisi ut commodo consequat.</p></div>
  <div class="vcol" style="left:196px;top:84px;width:56px"><svg class="ico"><use href="#g-pen"/></svg><b class="bt" style="margin-top:3px">Your Text Here</b><p class="lorem">Lorem ipsum dolor sit amet, consectetur adipiscing elit, sed do eiusmod incididunt ut labore et aliqua.</p><p class="lorem">Ut enimad minim veniam, quis nostrud exercitation laboris nisi ut commodo consequat.</p></div>
  <div class="footer"><span>Harborline © 2016 All rights reserved.</span><span>45</span></div>
</section>

<!-- 10 Photo left with text -->
<section class="slide">
  <div class="photo" role="img" aria-label="Banquet hall with chandeliers photograph" style="left:0;top:0;width:180px;bottom:12px;background:linear-gradient(90deg,#7d7468 0 40%,#5a4b3c 40%,#8a7157 70%,#4a3d30)"></div>
  <div class="abs" style="left:12px;top:44px;display:flex;align-items:center;gap:3px;font:400 6.5px 'Libre Baskerville',serif;color:#fff"><i style="display:block;width:8px;height:8px;border:.8px solid #fff"></i>Harborline Events</div>
  <div class="brand"><i></i>Harborline</div>
  <div class="col" style="left:190px;top:44px;width:64px"><div class="serif-head">Your Title Goes Here</div><p class="lorem">Lorem ipsum dolor sit amet, consectetur adipiscing elit, sed do eiusmod tempor incididunt ut labore et commodo consequat dolore magna aliqua.</p><p class="lorem">Duis aute irure dolor in reprehenderit in voluptate velit esse cillum dolore eu fugiat nulla pariatur.</p><p class="lorem">Ut enimad minim veniam, quis nostrud exercitation ullamco laboris nisi ut aliquip ex ea commodo consequat.</p></div>
  <div class="footer"><span>Harborline © 2016 All rights reserved.</span><span>46</span></div>
</section>

<!-- 11 Key Points Area -->
<section class="slide">
  <h2 class="title">Key Points Area</h2>
  <div class="brand"><i></i>Harborline</div>
  <p class="lorem abs" style="left:12px;top:52px;width:230px;font-size:3.9px;color:#888">Lorem ipsum dolor sit amet, consectetur adipiscing elit, sed do eiusmod tempor incididunt ut labore et dolore magna aliqua. Ut enimad minim veniam, quis nostrud exercitation ullamco laboris nisi ut aliquip ex ea commodo consequat.</p>
  <svg class="abs" style="left:22px;top:84px" width="222" height="50" viewBox="0 0 222 50" aria-hidden="true">
    <circle cx="25" cy="25" r="24" fill="var(--taupe)"/>
    <circle cx="68" cy="25" r="24" fill="var(--red)"/>
    <circle cx="111" cy="25" r="24" fill="var(--taupe)"/>
    <circle cx="154" cy="25" r="24" fill="var(--red)"/>
    <circle cx="197" cy="25" r="24" fill="var(--taupe)"/>
    <g fill="#fff" font-family="Roboto,sans-serif" font-size="4" text-anchor="middle">
      <circle cx="22" cy="17" r="2"/><circle cx="28" cy="17" r="2"/><text x="25" y="30">Visiting</text><text x="25" y="35">Customers</text>
      <path d="M62 17h12l-3 3h-6z"/><text x="68" y="30">Closing</text><text x="68" y="35">Ratio</text>
      <path d="M106 20v-3M109 20v-5M112 20v-4M115 20v-7" stroke="#fff" stroke-width="1.4"/><text x="111" y="30">Profit</text><text x="111" y="35">per Sale</text>
      <path d="M154 22l-4-4a2.3 2.3 0 014-2.6 2.3 2.3 0 014 2.6z"/><text x="154" y="30">Customers</text><text x="154" y="35">Satisfaction</text>
      <path d="M192 20l1-5 2 3 2-4 2 4 2-3 1 5z"/><text x="197" y="30">Branding</text><text x="197" y="35">Awareness</text>
    </g>
  </svg>
  <p class="lorem abs center" style="left:20px;top:144px;width:224px;font-size:3.9px;color:#888">Lorem ipsum dolor sit amet, consectetur adipiscing elit, sed do eiusmod tempor incididunt ut labore et dolore magna aliqua. Ut enimad minim veniam, quis nostrud exercitation ullamco laboris nisi ut aliquip ex ea commodo consequat.</p>
  <div class="footer"><span>Harborline © 2016 All rights reserved.</span><span>47</span></div>
</section>

<!-- 12 Your Title -->
<section class="slide">
  <h2 class="title">Your Title</h2>
  <div class="brand"><i></i>Harborline</div>
  <div class="photo" role="img" aria-label="Modern office interior photograph" style="left:88px;top:0;width:88px;bottom:12px;background:linear-gradient(180deg,#c9c5c0,#8a847c 50%,#3f3a35)"></div>
  <div class="col" style="left:12px;top:52px;width:68px"><div class="serif-head">Your Title Goes Here</div><p class="lorem">Lorem ipsum dolor sit amet, consectetur adipiscing elit, sed do eiusmod tempor incididunt ut labore et commodo consequat dolore magna aliqua.</p><p class="lorem">Duis aute irure dolor in reprehenderit in voluptate velit esse cillum dolore eu fugiat nulla pariatur.</p><p class="lorem">Ut enimad minim veniam, quis nostrud exercitation ullamco laboris nisi ut aliquip ex ea commodo consequat.</p></div>
  <div class="bullet" style="left:183px;top:50px;width:76px"><svg class="ico"><use href="#g-search"/></svg><div><b class="bt">Your Text Here</b><p class="lorem">Lorem ipsum dolor sit amet, adipiscing elit, sed do eiusmod.</p></div></div>
  <div class="bullet" style="left:183px;top:81px;width:76px"><svg class="ico"><use href="#g-pen"/></svg><div><b class="bt">Your Text Here</b><p class="lorem">Lorem ipsum dolor sit amet, adipiscing elit, sed do eiusmod.</p></div></div>
  <div class="bullet" style="left:183px;top:112px;width:76px"><svg class="ico"><use href="#g-pen"/></svg><div><b class="bt">Your Text Here</b><p class="lorem">Lorem ipsum dolor sit amet, adipiscing elit, sed do eiusmod.</p></div></div>
  <div class="bullet" style="left:183px;top:143px;width:76px"><svg class="ico"><use href="#g-gear"/></svg><div><b class="bt">Your Text Here</b><p class="lorem">Lorem ipsum dolor sit amet, adipiscing elit, sed do eiusmod.</p></div></div>
  <div class="footer"><span>Harborline © 2016 All rights reserved.</span><span>48</span></div>
</section>

<!-- 13 Bullet & Chart -->
<section class="slide">
  <h2 class="title">Bullet &amp; Chart Area</h2>
  <div class="brand"><i></i>Harborline</div>
  <svg class="abs" style="left:12px;top:58px" width="118" height="100" viewBox="0 0 118 100" aria-label="Bar chart of three series across four categories" role="img">
    <g font-family="Roboto,sans-serif" font-size="3.6" fill="#777">
      <text x="0" y="14">Category 4</text><text x="0" y="38">Category 3</text><text x="0" y="61">Category 2</text><text x="0" y="85">Category 1</text>
    </g>
    <line x1="37" y1="4" x2="37" y2="94" stroke="#ccc" stroke-width=".4"/>
    <rect x="37" y="6" width="82" height="3" fill="var(--taupe)"/><rect x="37" y="10" width="62" height="3" fill="var(--grey)"/><rect x="37" y="14" width="50" height="3" fill="var(--red)"/>
    <rect x="37" y="30" width="40" height="3" fill="var(--taupe)"/><rect x="37" y="34" width="22" height="3" fill="var(--grey)"/><rect x="37" y="38" width="56" height="3" fill="var(--red)"/>
    <rect x="37" y="53" width="52" height="3" fill="var(--taupe)"/><rect x="37" y="57" width="72" height="3" fill="var(--grey)"/><rect x="37" y="61" width="30" height="3" fill="var(--red)"/>
    <rect x="37" y="77" width="62" height="3" fill="var(--taupe)"/><rect x="37" y="81" width="34" height="3" fill="var(--grey)"/><rect x="37" y="85" width="92" height="3" fill="var(--red)"/>
    <g font-family="Roboto,sans-serif" font-size="3" fill="#777">
      <rect x="44" y="96" width="2" height="2" fill="var(--taupe)"/><text x="47" y="98">Series 3</text>
      <rect x="62" y="96" width="2" height="2" fill="var(--grey)"/><text x="65" y="98">Series 2</text>
      <rect x="80" y="96" width="2" height="2" fill="var(--red)"/><text x="83" y="98">Series 1</text>
    </g>
  </svg>
  <div class="bullet" style="left:157px;top:58px;width:100px"><svg class="ico"><use href="#g-search"/></svg><div><b class="bt">Your Text Here</b><p class="lorem">Lorem ipsum dolor sit amet, consectetur adipiscing elit, sed do eiusmod.</p></div></div>
  <div class="bullet" style="left:157px;top:87px;width:100px"><svg class="ico"><use href="#g-pen"/></svg><div><b class="bt">Your Text Here</b><p class="lorem">Lorem ipsum dolor sit amet, consectetur adipiscing elit, sed do eiusmod.</p></div></div>
  <div class="bullet" style="left:157px;top:115px;width:100px"><svg class="ico"><use href="#g-pen"/></svg><div><b class="bt">Your Text Here</b><p class="lorem">Lorem ipsum dolor sit amet, consectetur adipiscing elit, sed do eiusmod.</p></div></div>
  <div class="bullet" style="left:157px;top:143px;width:100px"><svg class="ico"><use href="#g-gear"/></svg><div><b class="bt">Your Text Here</b><p class="lorem">Lorem ipsum dolor sit amet, consectetur adipiscing elit, sed do eiusmod.</p></div></div>
  <div class="footer"><span>Harborline © 2016 All rights reserved.</span><span>49</span></div>
</section>

<!-- 14 Quote -->
<section class="slide">
  <div class="photo" role="img" aria-label="Audience in a conference hall photograph" style="inset:0;background:linear-gradient(180deg,#7c746b,#625a52 60%,#4f4842)"></div>
  <div class="abs" style="left:42px;top:62px;font:700 14px Georgia,serif;color:#fff">“</div>
  <div class="abs center" style="left:40px;right:40px;top:76px;font:400 8.6px 'Roboto',sans-serif;color:#fff;line-height:1.45">Coming together is a beginning.<br>Keeping together is progress.<br>Working together is success.</div>
  <div class="abs" style="right:52px;top:104px;font:700 14px Georgia,serif;color:#fff">”</div>
  <div class="abs center" style="left:0;right:0;top:123px;font-size:4.5px;color:#eee">~ Elias Warren ~</div>
</section>

<!-- 15 Text & Bullet -->
<section class="slide">
  <h2 class="title">Text &amp; Bullet Area</h2>
  <div class="brand"><i></i>Harborline</div>
  <div class="col" style="left:12px;top:52px;width:70px"><div class="serif-head">Your Title Goes Here</div><p class="lorem">Lorem ipsum dolor sit amet, consectetur adipiscing elit, sed do eiusmod tempor incididunt ut labore et commodo consequat dolore magna aliqua.</p><p class="lorem">Duis aute irure dolor in reprehenderit in voluptate velit esse cillum dolore eu fugiat nulla pariatur.</p><p class="lorem">Ut enimad minim veniam, quis nostrud exercitation ullamco laboris nisi ut aliquip ex ea commodo consequat.</p></div>
  <div class="bullet" style="left:90px;top:52px;width:80px"><svg class="ico"><use href="#g-search"/></svg><div><b class="bt">Your Text Here</b><p class="lorem">Lorem ipsum dolor sit amet, consectetur adipiscing elit, sed do eiusmod.</p></div></div>
  <div class="bullet" style="left:90px;top:80px;width:80px"><svg class="ico"><use href="#g-pen"/></svg><div><b class="bt">Your Text Here</b><p class="lorem">Lorem ipsum dolor sit amet, consectetur adipiscing elit, sed do eiusmod.</p></div></div>
  <div class="bullet" style="left:90px;top:108px;width:80px"><svg class="ico"><use href="#g-pen"/></svg><div><b class="bt">Your Text Here</b><p class="lorem">Lorem ipsum dolor sit amet, consectetur adipiscing elit, sed do eiusmod.</p></div></div>
  <div class="bullet" style="left:90px;top:136px;width:80px"><svg class="ico"><use href="#g-gear"/></svg><div><b class="bt">Your Text Here</b><p class="lorem">Lorem ipsum dolor sit amet, consectetur adipiscing elit, sed do eiusmod.</p></div></div>
  <div class="bullet" style="left:178px;top:52px;width:80px"><svg class="ico"><use href="#g-search"/></svg><div><b class="bt">Your Text Here</b><p class="lorem">Lorem ipsum dolor sit amet, consectetur adipiscing elit, sed do eiusmod.</p></div></div>
  <div class="bullet" style="left:178px;top:80px;width:80px"><svg class="ico"><use href="#g-pen"/></svg><div><b class="bt">Your Text Here</b><p class="lorem">Lorem ipsum dolor sit amet, consectetur adipiscing elit, sed do eiusmod.</p></div></div>
  <div class="bullet" style="left:178px;top:108px;width:80px"><svg class="ico"><use href="#g-pen"/></svg><div><b class="bt">Your Text Here</b><p class="lorem">Lorem ipsum dolor sit amet, consectetur adipiscing elit, sed do eiusmod.</p></div></div>
  <div class="bullet" style="left:178px;top:136px;width:80px"><svg class="ico"><use href="#g-gear"/></svg><div><b class="bt">Your Text Here</b><p class="lorem">Lorem ipsum dolor sit amet, consectetur adipiscing elit, sed do eiusmod.</p></div></div>
  <div class="footer"><span>Harborline © 2016 All rights reserved.</span><span>51</span></div>
</section>

<!-- 16 Pictures with Bullets -->
<section class="slide">
  <h2 class="title">Pictures with Bullets</h2>
  <div class="brand"><i></i>Harborline</div>
  <div class="photo" role="img" aria-label="Hotel exterior photograph" style="left:12px;top:46px;width:60px;height:36px;background:linear-gradient(180deg,#4a6aa0,#6b5b4b)"></div>
  <div class="photo" role="img" aria-label="Dining room photograph" style="left:72px;top:46px;width:60px;height:36px;background:linear-gradient(180deg,#a48466,#5b4632)"></div>
  <div class="photo" role="img" aria-label="Banquet hall photograph" style="left:132px;top:46px;width:60px;height:36px;background:linear-gradient(180deg,#7e6c5a,#3d342b)"></div>
  <div class="photo" role="img" aria-label="Ballroom with chandeliers photograph" style="left:192px;top:46px;width:60px;height:36px;background:linear-gradient(180deg,#b79a74,#5a4834)"></div>
  <svg class="ico abs" style="left:74px;top:57px"><use href="#g-search"/></svg>
  <svg class="ico abs" style="left:134px;top:57px"><use href="#g-gear"/></svg>
  <svg class="ico abs" style="left:194px;top:57px"><use href="#g-people"/></svg>
  <div class="col" style="left:17px;top:104px;width:110px"><div class="serif-head">Your Title Goes Here</div><p class="lorem">Lorem ipsum dolor sit amet, consectetur adipiscing elit, sed do eiusmod tempor incididunt ut labore et commodo consequat dolore magna aliqua.</p><p class="lorem">Duis aute irure dolor in reprehenderit in voluptate velit esse cillum dolore eu fugiat nulla pariatur.</p></div>
  <div class="col" style="left:141px;top:104px;width:110px"><div class="serif-head">Your Title Goes Here</div><p class="lorem">Lorem ipsum dolor sit amet, consectetur adipiscing elit, sed do eiusmod tempor incididunt ut labore et commodo consequat dolore magna aliqua.</p><p class="lorem">Duis aute irure dolor in reprehenderit in voluptate velit esse cillum dolore eu fugiat nulla pariatur.</p></div>
  <div class="footer"><span>Harborline © 2016 All rights reserved.</span><span>52</span></div>
</section>

<!-- 17 Table Area -->
<section class="slide">
  <h2 class="title">Table Area</h2>
  <div class="brand"><i></i>Harborline</div>
  <svg class="abs" style="left:12px;top:42px" width="240" height="130" viewBox="0 0 240 130" role="img" aria-label="Comparison table with two columns">
    <rect x="0" y="9" width="97" height="30" fill="var(--taupe)"/>
    <rect x="97" y="0" width="71" height="39" fill="var(--red)"/>
    <rect x="168" y="9" width="72" height="30" fill="var(--grey)"/>
    <g font-family="Roboto,sans-serif" font-weight="700" font-size="5" fill="#fff">
      <text x="6" y="27">Description</text>
      <text x="132" y="14" text-anchor="middle">Column 1</text>
      <text x="204" y="21" text-anchor="middle">Column 2</text>
    </g>
    <circle cx="132" cy="28" r="4" fill="#fff"/><circle cx="132" cy="28" r="1.6" fill="var(--red)"/>
    <circle cx="204" cy="31" r="3.5" fill="#fff" opacity=".7"/>
    <rect x="0" y="39" width="240" height="91" fill="#fff" stroke="#eee" stroke-width=".5"/>
    <g font-family="Roboto,sans-serif" font-size="3" fill="#666">
      <text x="6" y="47">Description 1</text><text x="6" y="56">Description 2</text><text x="6" y="65">Description 3</text><text x="6" y="74">Description 4</text>
      <text x="6" y="83">Description 5</text><text x="6" y="92">Description 6</text><text x="6" y="101">Description 7</text><text x="6" y="110">Description 8</text>
      <text x="132" y="84" text-anchor="middle">Text Column 1</text><text x="132" y="102" text-anchor="middle">Text Column 1</text>
      <text x="204" y="84" text-anchor="middle">Text Column 2</text><text x="204" y="102" text-anchor="middle">Text Column 2</text>
    </g>
    <g stroke="#e6e6e6" stroke-width=".4">
      <line x1="4" y1="49.5" x2="236" y2="49.5"/><line x1="4" y1="58.5" x2="236" y2="58.5"/><line x1="4" y1="67.5" x2="236" y2="67.5"/><line x1="4" y1="76.5" x2="236" y2="76.5"/>
      <line x1="4" y1="85.5" x2="236" y2="85.5"/><line x1="4" y1="94.5" x2="236" y2="94.5"/><line x1="4" y1="103.5" x2="236" y2="103.5"/><line x1="4" y1="112.5" x2="236" y2="112.5"/>
    </g>
    <g fill="#222">
      <circle cx="132" cy="46" r="1.1"/><circle cx="132" cy="55" r="1.1"/><circle cx="132" cy="73" r="1.1"/><circle cx="132" cy="91" r="1.1"/>
      <circle cx="204" cy="46" r="1.1"/><circle cx="204" cy="55" r="1.1"/><circle cx="204" cy="64" r="1.1"/><circle cx="204" cy="73" r="1.1"/><circle cx="204" cy="109" r="1.1"/>
    </g>
  </svg>
  <div class="footer"><span>Harborline © 2016 All rights reserved.</span><span>53</span></div>
</section>

<!-- 18 Thank You -->
<section class="slide">
  <div class="photo" role="img" aria-label="Muted meeting venue photograph" style="inset:0;background:linear-gradient(160deg,#9a9086,#7e756b)"></div>
  <div class="abs" style="left:14px;top:0;width:107px;bottom:0;background:var(--red)"></div>
  <div class="abs" style="left:28px;top:38px;display:flex;align-items:center;gap:3px;font:400 7px 'Libre Baskerville',serif;color:#fff"><i style="display:block;width:8px;height:8px;border:.8px solid #fff"></i>Harborline Events</div>
  <div class="abs" style="left:24px;top:78px;font:400 6.5px 'Libre Baskerville',serif;color:#fff">Our Contact</div>
  <div class="abs" style="left:24px;top:87px;width:18px;height:.6px;background:#fff"></div>
  <div class="abs" style="left:24px;top:98px;font-size:4.8px;color:#fff;line-height:1.3">
    <div style="display:flex;gap:5px;margin-bottom:8px"><svg width="6" height="6" viewBox="0 0 10 10" aria-hidden="true"><path d="M5 1l4 4H8v4H2V5H1z" fill="#fff"/></svg><span>42 Cedar Lane<br>Lenox, MA 01240</span></div>
    <div style="display:flex;gap:5px;margin-bottom:10px"><svg width="6" height="6" viewBox="0 0 10 10" aria-hidden="true"><path d="M2 1l2 2-1 1.5a6 6 0 002.5 2.5L7 6l2 2-1.5 1.5C4.5 9 1 5.5.5 2.5z" fill="#fff"/></svg><span>(555) 014-2290</span></div>
    <div style="display:flex;gap:5px;margin-bottom:10px"><svg width="6" height="6" viewBox="0 0 10 10" aria-hidden="true"><path d="M1 8l3-3 2 2 3-5" stroke="#fff" stroke-width="1.3" fill="none"/></svg><span>hello@harborline-events.com</span></div>
    <div style="display:flex;gap:5px"><svg width="6" height="6" viewBox="0 0 10 10" aria-hidden="true"><circle cx="5" cy="5" r="4" fill="none" stroke="#fff"/><path d="M1 5h8M5 1v8" stroke="#fff" stroke-width=".6"/></svg><span>www.harborline-events.com</span></div>
  </div>
  <div class="abs" style="left:52px;top:180px;display:flex;gap:6px">
    <span style="display:block;width:7px;height:7px;border-radius:50%;background:#fff"></span>
    <span style="display:block;width:7px;height:7px;border-radius:50%;background:#fff"></span>
    <span style="display:block;width:7px;height:7px;border-radius:50%;background:#fff"></span>
  </div>
  <div class="abs center" style="left:140px;width:110px;top:84px;font:700 14.5px 'Roboto',sans-serif;color:#fff">THANK YOU</div>
  <div class="abs center" style="left:140px;width:110px;top:102px;font:400 4.2px 'Libre Baskerville',serif;color:var(--red)">For Your Precious Time</div>
</section>

</main>
</body>
</html>
```